RESIDENTIAL CONSTRUCTION

We are a company that specializes in building custom residential homes, the design should also emphasize that quality and service is our priority.

Industry/Entity Type

Construction Company

Contact Information for Business Card

Contact Person: Tobias Kerrigan
Company Address: 243 West 9th St San Jose , Ca 95387
Phone Number : 408-736-2049
Email Address: Stonegatecrafts517@mailbrook.net

Font styles to use
Sans Serif

Colors
ec1f27

Requirements
Must have
• CSLB # 2736159
Nice to have
• needs to have same color as logo i uploaded, we will be printing these on a clear plastic card.

```html
<!DOCTYPE html>
<html lang="en">
<head>
<meta charset="utf-8">
<title>Stonegate Builders – Business Card</title>
<link href="https://fonts.googleapis.com/css2?family=Oswald:wght@500;600&family=Lato:wght@400&display=swap" rel="stylesheet">
<style>
  :root {
    --brand-red: #c01f2e;
    --ink-black: #0b0b0b;
    --card-white: #f7f6f5;
    --page-bg: #e4e2e0;
    --text-light: #ffffff;
  }
  html, body {
    margin: 0;
    width: 1200px;
    height: 900px;
    overflow: hidden;
    background: var(--page-bg);
  }
  .card {
    position: absolute;
    left: 110px;
    top: 145px;
    width: 980px;
    height: 610px;
    background: var(--card-white);
    box-shadow: 0 8px 30px rgba(0,0,0,0.12);
    overflow: hidden;
  }
  .brand {
    position: absolute;
    left: 0;
    right: 0;
    top: 112px;
    display: flex;
    justify-content: center;
    align-items: center;
    gap: 18px;
  }
  .brand-square {
    width: 52px;
    height: 52px;
    background: var(--brand-red);
  }
  .brand-name {
    font-family: "Oswald", sans-serif;
    font-weight: 600;
    font-size: 72px;
    line-height: 1;
    letter-spacing: 1px;
    color: var(--brand-red);
    text-transform: uppercase;
  }
  .info-band {
    position: absolute;
    left: 0;
    top: 330px;
    width: 980px;
    height: 280px;
  }
  .info-band svg { display: block; }
  .contact-name {
    position: absolute;
    left: 42px;
    top: 372px;
    margin: 0;
    font-family: "Oswald", sans-serif;
    font-weight: 500;
    font-size: 34px;
    line-height: 1;
    color: var(--text-light);
    text-transform: uppercase;
  }
  .address {
    position: absolute;
    left: 42px;
    top: 445px;
    margin: 0;
    font-family: "Lato", sans-serif;
    font-style: normal;
    font-size: 27px;
    line-height: 35px;
    color: var(--text-light);
  }
  .contact-lines {
    position: absolute;
    right: 36px;
    top: 392px;
    text-align: right;
    font-family: "Lato", sans-serif;
    font-size: 26px;
    line-height: 35px;
    color: var(--text-light);
  }
  .license {
    position: absolute;
    right: 36px;
    top: 538px;
    font-family: "Lato", sans-serif;
    font-size: 26px;
    line-height: 35px;
    color: var(--text-light);
  }
</style>
</head>
<body>
  <div class="card">
    <div class="brand">
      <span class="brand-square"></span>
      <span class="brand-name">Stonegate Builders</span>
    </div>

    <div class="info-band">
      <svg width="980" height="280" viewBox="0 0 980 280">
        <rect class="band-red" x="0" y="0" width="980" height="280" fill="#c01f2e"/>
        <polygon class="band-black" points="0,0 403,0 250,280 0,280" fill="#0b0b0b"/>
      </svg>
    </div>

    <h1 class="contact-name">Tobias Kerrigan</h1>
    <address class="address">243 West<br>9th St San Jose<br>Ca 95387</address>

    <div class="contact-lines">
      <div class="email">Stonegatecrafts517@mailbrook.net</div>
      <div class="phone">408-736-2049</div>
    </div>
    <div class="license">CSLB # 2736159</div>
  </div>
</body>
</html>
```